Massage Therapy Business Card

I’d like the same exact business card (same graphics and colors) that I uploaded by R & K Designer with:
Name of the business: Bodywork by Delmar;
Delmar Hollis (Massage Therapist);
Contact: (555)-418-2073
Email: bodyworkbydelmar@quillmail.test;
IG: @Gr4in_bodywork

On the back Please add:
1. Mobile Sessions available upon request
2. Book 3 Massages, Get 4th 50% off

Target Market(s)

Adults ages 21+

Industry/Entity Type

Healthcare and Therapy

Contact Information for Business Card

The color should be different shades of blue with a logo of a male anatomy and pressure points for massages

Colors
0054AA
0677BA
7BADD7
CADEEF
E8F1F8
0094D4
00A9DD
6FCCEA
C7EBF8
E9F6FB
00AB8E
00BBA5
67D7C9
C6EFE9
E9F9F6
EB3D1F
EC4F4E
F09395
F8D3D4
FCEDEE

Requirements
Must have
• Must be Double Sided
Nice to have
• Newer Modern look with a Masculine Feel

```html
<!DOCTYPE html>
<html lang="en">
<head>
<meta charset="utf-8">
<title>Bodywork by Delmar – Business Card</title>
<link rel="stylesheet" href="https://fonts.googleapis.com/css2?family=Poppins:wght@400;500;600&family=Montserrat:wght@500;600&family=Roboto+Condensed:wght@700;800&display=swap">
<style>
  :root{
    --blue-deep:#0054AA;
    --blue-main:#0677BA;
    --blue-bright:#0094D4;
    --blue-sky:#00A9DD;
    --blue-light:#6FCCEA;
    --blue-pale:#C7EBF8;
    --ink:#1e2a36;
    --white:#ffffff;
    --paper:#f4f5f7;
    --red:#EB3D1F;
    --red-soft:#EC4F4E;
    --orange:#f57a1c;
    --bg:#d6d8db;
  }
  *{box-sizing:border-box;margin:0;padding:0}
  html,body{width:1200px;height:800px;overflow:hidden;background:var(--bg)}
  .stage{width:1200px;height:800px;display:flex;flex-direction:column;align-items:center;justify-content:center;gap:28px}
  .card{position:relative;width:640px;height:366px;border-radius:22px;overflow:hidden;background:var(--paper);box-shadow:0 6px 18px rgba(0,0,0,.18)}

  /* front */
  .front__art{position:absolute;right:0;top:0;width:300px;height:366px;
    background:radial-gradient(ellipse 38% 60% at 55% 50%, rgba(245,122,28,.85) 0%, rgba(245,122,28,.35) 30%, transparent 55%),
               radial-gradient(ellipse 60% 75% at 55% 48%, var(--blue-light) 0%, var(--blue-sky) 45%, rgba(0,169,221,0) 80%);}
  .brand{position:absolute;left:44px;top:56px;display:flex;align-items:center;gap:14px}
  .brand__dot{width:58px;height:58px;border-radius:50%;background:var(--blue-main);flex:none}
  .brand__name{font-family:"Poppins",sans-serif;font-weight:500;font-size:26px;line-height:1.1;color:var(--blue-main);letter-spacing:.02em}
  .person{position:absolute;left:46px;top:158px}
  .person__name{font-family:"Poppins",sans-serif;font-weight:600;font-size:26px;color:var(--blue-main);line-height:1.1}
  .person__role{font-family:"Poppins",sans-serif;font-weight:500;font-size:14px;color:var(--ink);margin-top:2px}
  .contacts{position:absolute;left:46px;top:250px;list-style:none}
  .contacts li{display:flex;align-items:center;gap:10px;font-family:"Poppins",sans-serif;font-size:14px;color:var(--ink);margin-bottom:6px}
  .contacts .ico{width:18px;height:18px;border-radius:50%;background:var(--blue-main);display:flex;align-items:center;justify-content:center;flex:none}
  .contacts svg{width:10px;height:10px}

  /* back */
  .back{background:linear-gradient(100deg,var(--paper) 0%,var(--paper) 27%,var(--blue-bright) 42%,var(--blue-main) 100%)}
  .back__art{position:absolute;left:0;top:0;width:250px;height:366px;
    background:radial-gradient(circle at 55% 70%, rgba(255,170,60,.7) 0%, transparent 18%),
               radial-gradient(ellipse 55% 75% at 45% 55%, var(--blue-deep) 0%, rgba(0,84,170,.55) 50%, transparent 80%);}
  .headline{position:absolute;left:260px;right:30px;top:58px;text-align:center;font-family:"Montserrat",sans-serif;font-weight:500;font-size:27px;line-height:1.08;color:var(--white);letter-spacing:.01em}
  .offer{position:absolute;left:252px;top:196px}
  .offer__title{font-family:"Roboto Condensed",sans-serif;font-weight:800;font-size:28px;line-height:1.1;color:var(--white);letter-spacing:.01em}
  .steps{display:flex;gap:10px;margin-top:14px}
  .step{width:64px;height:64px;border-radius:50%;background:radial-gradient(circle at 40% 35%,#ffffff 0%,#e4e6e8 45%,#b9bdc2 100%);display:flex;align-items:center;justify-content:center;font-family:"Roboto Condensed",sans-serif;font-weight:800;font-size:34px;color:var(--red)}
  .badge{position:absolute;right:28px;top:190px;width:100px;height:100px;border-radius:50%;background:radial-gradient(circle at 40% 35%,var(--red-soft),var(--red) 70%);display:flex;flex-direction:column;align-items:center;justify-content:center;color:var(--white);font-family:"Montserrat",sans-serif;line-height:1}
  .badge__top{font-size:12px;font-weight:600}
  .badge__big{font-family:"Roboto Condensed",sans-serif;font-weight:800;font-size:32px;margin:2px 0}
  .badge__bottom{font-size:16px;font-weight:600}
</style>
</head>
<body>
<main class="stage">
  <section class="card front">
    <div class="front__art" role="img" aria-label="Illustration of a male figure from behind with an x-ray skeleton and the spine highlighted in orange"></div>
    <div class="brand">
      <span class="brand__dot"></span>
      <span class="brand__name">BODYWORK<br>by Delmar</span>
    </div>
    <div class="person">
      <p class="person__name">Delmar Hollis</p>
      <p class="person__role">Massage Therapist</p>
    </div>
    <ul class="contacts">
      <li><span class="ico"><svg viewBox="0 0 10 10"><path d="M2 1l2 2-1 1c.6 1.3 1.7 2.4 3 3l1-1 2 2-1.3 1.2C4.6 9 1 5.4.8 2.3z" fill="#fff"/></svg></span>(555)-418-2073</li>
      <li><span class="ico"><svg viewBox="0 0 10 10"><rect x="1" y="2.5" width="8" height="5" fill="none" stroke="#fff" stroke-width="1"/><path d="M1 2.5l4 3 4-3" fill="none" stroke="#fff" stroke-width="1"/></svg></span>bodyworkbydelmar@quillmail.test</li>
      <li><span class="ico"></span>@Gr4in_bodywork</li>
    </ul>
  </section>

  <section class="card back">
    <div class="back__art" role="img" aria-label="Illustration of a blue x-ray figure bending down with glowing knee and ankle joints"></div>
    <h2 class="headline">MOBILE SESSIONS<br>AVAILABLE UPON<br>REQUEST</h2>
    <div class="offer">
      <p class="offer__title">BOOK 3 MASSAGES</p>
      <div class="steps">
        <span class="step">1</span>
        <span class="step">2</span>
        <span class="step">3</span>
      </div>
    </div>
    <div class="badge">
      <span class="badge__top">GET 4TH</span>
      <span class="badge__big">50%</span>
      <span class="badge__bottom">OFF</span>
    </div>
  </section>
</main>
</body>
</html>
```